Marrowby Nature Alliance needs a fundraiser poster

We are having an annual awards night and fundraiser.

On the top of the poster please put "Marrowby Nature Alliance Annual Awards Night and Fundraiser"

Date: March 25, 2023
Time: 6:00pm doors open. Supper at 7:00pm
Location: Quenford Sportsdome Auditorium
Cost: $40 for Adults, $20 for 18 and under

We also would like on the poster, "Live Auctions, Silent auctions, and raffles"
"Serving Elk, Moose, and Wild Boar. Also beef"

```html
<!DOCTYPE html>
<html lang="en">
<head>
<meta charset="utf-8">
<title>Marrowby Nature Alliance Annual Awards Night and Fundraiser</title>
<link rel="stylesheet" href="https://fonts.googleapis.com/css2?family=Cinzel:wght@600;700&family=Montserrat:wght@500;600;900&display=swap">
<style>
  :root {
    --orange: #f04b2e;
    --navy: #0a1124;
    --ink: #111111;
    --white: #ffffff;
    --forest-grey: #7b7b7b;
  }
  * { margin: 0; padding: 0; box-sizing: border-box; }
  html, body { width: 900px; height: 1200px; overflow: hidden; background: var(--white); }
  .poster {
    position: relative;
    width: 900px;
    height: 1200px;
    overflow: hidden;
    background: var(--white);
    font-family: "Montserrat", sans-serif;
  }
  .org-name {
    position: absolute;
    left: 40px;
    top: 110px;
    width: 320px;
    font-family: "Cinzel", serif;
    font-weight: 700;
    font-size: 42px;
    line-height: 1.15;
    color: var(--ink);
    text-align: center;
  }
  .event-title {
    position: absolute;
    left: 382px;
    top: 78px;
    font-family: "Cinzel", serif;
    font-weight: 700;
    font-size: 62px;
    line-height: 54px;
    letter-spacing: 1px;
    color: var(--orange);
    text-transform: uppercase;
  }
  .roofline {
    position: absolute;
    left: 0;
    top: 0;
    width: 900px;
    height: 1200px;
  }
  .event-body {
    position: absolute;
    left: 0;
    top: 0;
    width: 900px;
    height: 1200px;
  }
  .details {
    position: absolute;
    left: 0;
    top: 466px;
    width: 900px;
    text-align: center;
    color: var(--white);
    font-weight: 600;
    font-size: 47px;
    line-height: 61px;
    text-transform: none;
  }
  .venue-rule {
    position: absolute;
    left: 84px;
    width: 744px;
    height: 3px;
    background: var(--white);
  }
  .venue-rule.top { top: 671px; }
  .venue-rule.bottom { top: 748px; }
  .venue {
    position: absolute;
    left: 0;
    top: 683px;
    width: 900px;
    text-align: center;
    font-weight: 900;
    font-size: 40px;
    line-height: 56px;
    color: var(--navy);
    letter-spacing: -0.5px;
  }
  .pricing {
    position: absolute;
    left: 31px;
    top: 796px;
    width: 838px;
    height: 70px;
    background: var(--navy);
    color: var(--white);
    font-weight: 600;
    font-size: 31px;
    line-height: 70px;
    text-align: center;
    letter-spacing: 1px;
  }
  .treeline {
    position: absolute;
    left: 0;
    top: 905px;
    width: 900px;
    height: 180px;
    background: linear-gradient(to bottom, var(--orange) 0%, #5a2a2a 45%, var(--navy) 85%);
  }
  .footer-band {
    position: absolute;
    left: 0;
    top: 1084px;
    width: 900px;
    height: 116px;
    background: var(--navy);
  }
  .highlights {
    position: absolute;
    left: 0;
    top: 1092px;
    width: 900px;
    text-align: center;
    font-family: "Cinzel", serif;
    font-weight: 700;
    font-size: 25px;
    line-height: 35px;
    color: var(--white);
  }
</style>
</head>
<body>
<main class="poster">
  <svg class="roofline" width="900" height="1200" viewBox="0 0 900 1200" aria-hidden="false">
    <polygon role="img" aria-label="Grey pine forest silhouette along the horizon" points="0,352 900,336 900,420 471,362 0,436" fill="var(--forest-grey)"/>
    <polygon points="0,472 471,396 900,467 900,1200 0,1200" fill="var(--orange)"/>
    <polygon points="0,434 471,360 900,418 900,467 471,396 0,472" fill="var(--ink)"/>
    <polygon points="0,445 471,371 900,429 900,437 471,379 0,453" fill="var(--white)"/>
  </svg>

  <div class="org-name">Marrowby Nature Alliance</div>

  <h1 class="event-title">Annual<br>Awards<br>Night and<br>Fundraiser</h1>

  <section class="event-body">
    <p class="details">MARCH 25, 2023<br>6:00pm DOORS OPEN<br>SUPPER @7:00pm</p>
    <div class="venue-rule top"></div>
    <p class="venue">Quenford Sportsdome Auditorium</p>
    <div class="venue-rule bottom"></div>
    <p class="pricing">$40 FOR ADULTS&nbsp; $20 for 18 AND UNDER</p>
    <div class="treeline" role="img" aria-label="Dark navy pine forest silhouette against the orange sky"></div>
    <div class="footer-band"></div>
    <p class="highlights">"Live Auctions, Silent auctions, and raffles"<br>"Serving Elk, Moose, and Wild Boar. Also beef"</p>
  </section>
</main>
</body>
</html>
```